Business cards for Harbourline Supply Pty Ltd that import building products into Australia from China
Target Market(s)
Business to Business
Industry/Entity Type
Business
Contact Information for Business Card
Front: Logo and Business Name
Rear:
Vernon Ashcombe
General Manager
Mobile: 0427 619 354
email: vern@harbourlinesupply.com.au
alternative email: vern@coastwardgoods.com.au
web: www.harbourlinesupply.com.au
Adelaide, Brisbane and Darwin
Colors
ec1f27
fbee3d

```html
<!DOCTYPE html>
<html lang="en">
<head>
<meta charset="utf-8">
<title>Harbourline Supply – Business Cards</title>
<link href="https://fonts.googleapis.com/css2?family=Open+Sans:wght@400;600;700;800&display=swap" rel="stylesheet">
<style>
  :root {
    --orange: #f39320;
    --charcoal: #252527;
    --white: #ffffff;
    --backdrop: #d9d9db;
    --card-w: 620px;
    --card-h: 379px;
  }
  * { box-sizing: border-box; margin: 0; padding: 0; }
  html, body {
    width: 1200px;
    height: 977px;
    overflow: hidden;
    background: var(--backdrop);
    font-family: "Open Sans", sans-serif;
  }
  .sheet {
    width: 1200px;
    height: 977px;
    display: flex;
    flex-direction: column;
    align-items: center;
    justify-content: center;
    gap: 60px;
  }
  .card {
    width: var(--card-w);
    height: var(--card-h);
    position: relative;
    overflow: hidden;
    box-shadow: 0 6px 18px rgba(0,0,0,0.18);
  }

  /* Brand lockup */
  .brand {
    display: flex;
    align-items: center;
    gap: 16px;
  }
  .brand-square {
    width: 58px;
    height: 58px;
    flex: none;
  }
  .brand-name {
    font-weight: 800;
    font-size: 38px;
    letter-spacing: 0.5px;
    line-height: 1;
    text-transform: uppercase;
    white-space: nowrap;
  }

  /* Front */
  .card-front {
    background: var(--orange);
    display: flex;
    flex-direction: column;
    align-items: center;
    justify-content: center;
    color: var(--white);
  }
  .card-front .brand-square { background: var(--white); }
  .card-front .brand-name { color: var(--white); }
  .locations {
    position: absolute;
    bottom: 52px;
    left: 0;
    right: 0;
    text-align: center;
    font-weight: 600;
    font-size: 14px;
    letter-spacing: 1.2px;
    text-transform: uppercase;
  }
  .locations .divider { margin: 0 12px; }

  /* Back */
  .card-back { background: var(--white); }
  .back-top {
    height: 222px;
    display: flex;
    align-items: center;
    justify-content: center;
  }
  .card-back .brand-square { background: var(--orange); width: 50px; height: 50px; }
  .card-back .brand-name { color: var(--charcoal); font-size: 32px; }
  .name-band {
    height: 50px;
    background: var(--orange);
    color: var(--white);
    display: flex;
    align-items: flex-end;
    padding: 0 0 10px 200px;
    white-space: nowrap;
  }
  .person-name { font-weight: 700; font-size: 19px; }
  .person-role { font-weight: 600; font-size: 13px; margin-left: 6px; }
  .band-rule { height: 4px; background: var(--white); }
  .back-bottom {
    height: calc(var(--card-h) - 222px - 50px - 4px);
    background: var(--charcoal);
    color: var(--white);
    display: flex;
    justify-content: space-between;
    align-items: flex-start;
    padding: 14px 28px 0 96px;
    font-size: 13.5px;
  }
  .contact-list { list-style: none; display: flex; flex-direction: column; gap: 6px; }
  .contact-list--left { margin-top: 24px; }
  .contact-list li { display: flex; align-items: center; gap: 10px; white-space: nowrap; }
  .contact-list svg { width: 14px; height: 14px; flex: none; }
  .icon-solid { fill: var(--white); }
  .icon-envelope { fill: var(--white); }
  .icon-envelope .flap { fill: none; stroke: var(--charcoal); stroke-width: 2; }
  .icon-globe { fill: var(--white); }
  .icon-globe .grid { fill: none; stroke: var(--charcoal); stroke-width: 1.6; }
</style>
</head>
<body>
<main class="sheet">

  <section class="card card-front" aria-label="Card front">
    <div class="brand">
      <span class="brand-square"></span>
      <span class="brand-name">Harbourline Supply</span>
    </div>
    <p class="locations">Adelaide<span class="divider">|</span>Brisbane<span class="divider">|</span>Darwin</p>
  </section>

  <section class="card card-back" aria-label="Card back">
    <div class="back-top">
      <div class="brand">
        <span class="brand-square"></span>
        <span class="brand-name">Harbourline Supply</span>
      </div>
    </div>
    <div class="name-band">
      <span class="person-name">Vernon Ashcombe,</span>
      <span class="person-role">General Manager</span>
    </div>
    <div class="band-rule"></div>
    <div class="back-bottom">
      <ul class="contact-list contact-list--left">
        <li>
          <svg class="icon-solid" viewBox="0 0 24 24" aria-hidden="true"><path d="M6.6 10.8a15.1 15.1 0 0 0 6.6 6.6l2.2-2.2c.3-.3.7-.4 1-.2 1.1.4 2.3.6 3.6.6.6 0 1 .4 1 1V20c0 .6-.4 1-1 1C10.6 21 3 13.4 3 4c0-.6.4-1 1-1h3.5c.6 0 1 .4 1 1 0 1.3.2 2.5.6 3.6.1.3 0 .7-.2 1z"/></svg>
          <span>0427 619 354</span>
        </li>
        <li>
          <svg class="icon-envelope" viewBox="0 0 24 24" aria-hidden="true"><rect x="2" y="5" width="20" height="14"/><path class="flap" d="M2 6l10 7 10-7"/></svg>
          <span>vern@harbourlinesupply.com.au</span>
        </li>
      </ul>
      <ul class="contact-list contact-list--right">
        <li>
          <svg class="icon-envelope" viewBox="0 0 24 24" aria-hidden="true"><rect x="2" y="5" width="20" height="14"/><path class="flap" d="M2 6l10 7 10-7"/></svg>
          <span>vern@coastwardgoods.com.au</span>
        </li>
        <li>
          <svg class="icon-globe" viewBox="0 0 24 24" aria-hidden="true"><circle cx="12" cy="12" r="10"/><path class="grid" d="M2 12h20M12 2c3 3 3 17 0 20M12 2c-3 3-3 17 0 20"/></svg>
          <span>www.harbourlinesupply.com.au</span>
        </li>
      </ul>
    </div>
  </section>

</main>
</body>
</html>
```